Modern Innovative Business Card Design

We require a nice, modern, clean business card design, ready for upload to Cardomora. Our company develops online banking software solutions for small financial insitutions. The design should be clean, professional, but yet not "corporate boring". See www.fyrolt.com for an idea of business image and profile. The design should communicate innovation, be modern and fresh, yet look professional and established.

Target Market(s)

Finance industry, bankers, entrepreneurs

Industry/Entity Type

Financial

Contact Information for Business Card

Tobias Wendlerup
CEO

FYROLT BV
Lindenwerf 38
1027 HX Amsterdam
The Netherlands

Phone: +31 20 517 8036
Direct: +31 20 604 1758
Skype: tobias.fyrolt
ceo@fyrolt.com
www.fyrolt.com

Font styles to use
Sans Serif

Requirements
Must have
• Should look clean, modern and professional. File should be ready for upload to cardomora.
Should not have
• Boring standard corporate layout

```html
<!DOCTYPE html>
<html lang="en">
<head>
<meta charset="utf-8">
<title>FYROLT – Business Card</title>
<link rel="stylesheet" href="https://fonts.googleapis.com/css2?family=Open+Sans:wght@400;600;700&display=swap">
<style>
  :root {
    --backdrop: #3b3140;
    --card: #fbfbfa;
    --ink: #4a4a4a;
    --ink-soft: #5c5c5c;
    --swoosh: #5a5a5a;
    --green: #8dc63f;
    --green-light: #b4dc7e;
    --on-green: #2f3a1f;
    --white: #ffffff;
  }
  * { margin: 0; padding: 0; box-sizing: border-box; }
  html, body {
    width: 1200px; height: 800px; overflow: hidden;
    background: var(--backdrop);
    font-family: "Open Sans", Arial, sans-serif;
  }
  .card {
    position: absolute; left: 180px; top: 160px;
    width: 840px; height: 480px;
    background: var(--card);
    overflow: hidden;
    box-shadow: 0 18px 40px rgba(0,0,0,.35);
  }
  .card-shapes { position: absolute; inset: 0; }
  .brand {
    position: absolute; left: 64px; top: 52px;
    font-weight: 600; font-size: 64px; letter-spacing: 8px;
    color: var(--ink); line-height: 1;
  }
  .holder {
    position: absolute; left: 92px; top: 160px;
    font-size: 19px; color: var(--ink);
  }
  .holder-name { font-weight: 700; }
  .holder-role { font-size: 14px; }
  .address {
    position: absolute; left: 64px; top: 330px;
    font-size: 15px; line-height: 1.45; color: var(--ink-soft);
    font-style: normal;
  }
  .brand-echo {
    position: absolute; left: 612px; top: 198px;
    font-weight: 600; font-size: 36px; letter-spacing: 5px;
    color: var(--green-light); line-height: 1;
  }
  .contacts {
    position: absolute; left: 548px; top: 262px;
    font-size: 16px; line-height: 1.5; color: var(--on-green);
  }
  .contact-row { display: flex; }
  .contact-label { width: 62px; }
  .contact-sep { width: 16px; }
  .website {
    position: absolute; left: 548px; top: 400px;
    font-weight: 700; font-size: 18px; color: var(--white);
  }
</style>
</head>
<body>
  <main class="card">
    <svg class="card-shapes" width="840" height="480" viewBox="0 0 840 480" aria-hidden="true">
      <path class="swoosh" fill="var(--swoosh)"
            d="M262,480 C350,270 570,110 840,68 C580,112 400,270 308,480 Z"/>
      <path class="green-field" fill="var(--green)"
            d="M840,100 C600,130 420,280 330,480 L840,480 Z"/>
    </svg>

    <div class="brand">FYROLT</div>

    <div class="holder">
      <span class="holder-name">Tobias Wendlerup</span>
      <span class="holder-role"> - CEO</span>
    </div>

    <address class="address">
      FYROLT BV Lindenwerf 38 1027 HX<br>
      Amsterdam The Netherland
    </address>

    <div class="brand-echo">FYROLT</div>

    <div class="contacts">
      <div class="contact-row"><span class="contact-label">Phone</span><span class="contact-sep">:</span><span>+31 20 517 8036</span></div>
      <div class="contact-row"><span class="contact-label">Direct</span><span class="contact-sep">:</span><span>+31 20 604 1758</span></div>
      <div class="contact-row"><span class="contact-label">Email</span><span class="contact-sep">:</span><span>ceo@fyrolt.com</span></div>
      <div class="contact-row"><span class="contact-label">Skype</span><span class="contact-sep">:</span><span>tobias.fyrolt</span></div>
    </div>

    <div class="website">www.fyrolt.com</div>
  </main>
</body>
</html>
```